Professional stationery for boutique management consulting business

I need branded business stationery for my consulting business, using our existing logo and website branding. We consult to senior executives to create deep cultural change needed for humane, people-centred workplaces. The key deliverables are: (A4 size) business letterheads, proposal cover, project folder, report template, email footer, business card, simple powerpoint template. A warm, empowering and expert tone of voice is important as it needs to bridge the gap between academia and industry. It should be clean and professional without feeling "over-branded".
I would like to see stationery designs that use my website colours and design elements (see attached file), especially the delta logo. Our fonts are Operetta and Sofia Pro.
Updates

Thanks for the designs sent so far. Just to confirm that our key deliverables for this project are: - (A4 size) business letterhead - (A4 size) proposal template - (A4 size) report template - Project folder, - Simple powerpoint template - Business card Many thanks

Target Market(s)

Senior executives and business professionals with an interest in business school thinking.

Industry/Entity Type

Management consulting and executive coaching

Font styles to use
Other font styles liked:
• Operetta and Sofia Pro

Colors
0054AA
0677BA
7BADD7
CADEEF
E8F1F8

Requirements
Must have
• Clean professional design that ties in closely to complement and extend the design elements in my website: brantlowadvisory.com
Nice to have
• Address and contact details I can edit in Microsoft Word, Outlook for Mac, etc
Should not have
• Excessive brand elements, fussy design and additional colours.

```html
<!DOCTYPE html>
<html lang="en">
<head>
<meta charset="utf-8">
<title>Brantlow Advisory — Business Card</title>
<link href="https://fonts.googleapis.com/css2?family=Playfair+Display:wght@400&family=Roboto:wght@400;500;700&display=swap" rel="stylesheet">
<style>
  :root {
    --navy: #1c2268;
    --ink: #3a3a40;
    --paper: #f3f3f1;
    --backdrop: #ccd1d2;
    --rule: #9a9aa2;
  }
  * { box-sizing: border-box; margin: 0; padding: 0; }
  html, body { width: 1200px; height: 1051px; overflow: hidden; }
  body {
    background: var(--backdrop);
    font-family: "Roboto", sans-serif;
    display: flex;
    flex-direction: column;
    align-items: center;
    justify-content: center;
    gap: 70px;
  }
  .card {
    width: 590px;
    height: 337px;
    background: var(--paper);
    position: relative;
    box-shadow: 0 2px 6px rgba(0,0,0,0.12);
  }
  .card--back { border-bottom: 6px solid var(--navy); }

  .wordmark {
    display: flex;
    align-items: flex-start;
    gap: 14px;
    color: var(--navy);
  }
  .wordmark__square {
    background: var(--navy);
    flex: none;
  }
  .wordmark__name {
    font-family: "Playfair Display", serif;
    font-weight: 400;
    line-height: 0.92;
    color: var(--navy);
  }

  /* back */
  .card--back .wordmark {
    position: absolute;
    left: 120px;
    top: 92px;
  }
  .card--back .wordmark__square { width: 34px; height: 34px; margin-top: 10px; }
  .card--back .wordmark__name { font-size: 58px; }
  .card--back .site {
    position: absolute;
    left: 168px;
    top: 244px;
    font-size: 15px;
    color: var(--ink);
    letter-spacing: 0.3px;
  }

  /* front */
  .card--front .wordmark {
    position: absolute;
    left: 40px;
    top: 92px;
  }
  .card--front .wordmark__square { width: 20px; height: 20px; margin-top: 6px; }
  .card--front .wordmark__name { font-size: 36px; }
  .divider {
    position: absolute;
    left: 300px;
    top: 90px;
    width: 2px;
    height: 190px;
    background: linear-gradient(var(--rule) 0 22px, transparent 22px 34px, var(--rule) 34px 100%);
  }
  .contact {
    position: absolute;
    left: 322px;
    top: 90px;
    color: var(--ink);
    font-size: 14px;
    line-height: 1.3;
  }
  .contact__org {
    font-weight: 700;
    color: var(--navy);
    font-size: 15px;
    letter-spacing: 0.3px;
    text-transform: uppercase;
  }
  .contact__role { font-weight: 500; margin-bottom: 8px; }
  .contact__address { margin-bottom: 8px; }
  .contact__line { display: flex; align-items: center; gap: 8px; }
  .contact__line svg { width: 13px; height: 13px; flex: none; fill: var(--navy); }
</style>
</head>
<body>

  <section class="card card--back" aria-label="Business card, back">
    <div class="wordmark">
      <span class="wordmark__square"></span>
      <span class="wordmark__name">Brantlow<br>Advisory</span>
    </div>
    <p class="site">www.brantlowadvisory.com</p>
  </section>

  <section class="card card--front" aria-label="Business card, front">
    <div class="wordmark">
      <span class="wordmark__square"></span>
      <span class="wordmark__name">Brantlow<br>Advisory</span>
    </div>
    <div class="divider"></div>
    <div class="contact">
      <p class="contact__org">Northfield Practice</p>
      <p class="contact__role">Managing Director</p>
      <p class="contact__address">Suite 412/88 Linden St<br>Fitzroy, Victoria<br>Australia</p>
      <p class="contact__line">
        <svg viewBox="0 0 24 24"><path d="M6.6 10.8a15.1 15.1 0 0 0 6.6 6.6l2.2-2.2c.3-.3.7-.4 1-.2 1.1.4 2.3.6 3.6.6.6 0 1 .4 1 1V20c0 .6-.4 1-1 1A17 17 0 0 1 3 4c0-.6.4-1 1-1h3.5c.6 0 1 .4 1 1 0 1.3.2 2.5.6 3.6.1.3 0 .7-.2 1z"/></svg>
        +61 3 5550 1274
      </p>
      <p class="contact__line">
        <svg viewBox="0 0 24 24"><path d="M2 5h20v14H2z M2 5l10 8 10-8" fill="none" stroke="currentColor" stroke-width="0"/><path d="M2 5h20l-10 8z M2 7l10 8 10-8v12H2z"/></svg>
        info@brantlowadvisory.com
      </p>
      <p class="contact__line">
        <svg viewBox="0 0 24 24"><circle cx="12" cy="12" r="9.5" fill="none" stroke="#1c2268" stroke-width="2"/><path d="M2.5 12h19M12 2.5c3 3 3 16 0 19M12 2.5c-3 3-3 16 0 19" fill="none" stroke="#1c2268" stroke-width="1.6"/></svg>
        www.brantlowadvisory.com
      </p>
    </div>
  </section>

</body>
</html>
```